Banner design to promote upcoming Internet meeting

I have an Internet-related meeting coming up and I need a free-standing vinyl banner designed for it. If you do a good job, I'll need similar banners for several other meetings, for which I'll pay separately. The specifications for the banner are in the attached PDF file.

The main heading of the banner, bigger than the logos, should say "Unified Marrowby Roundtable" and in smaller text "Halvern Policy Symposium", "Guadalajara", and "December 2016". The design should communicate "Internet" but in a subtle and classy way.

Target Market(s)

Professionals

Industry/Entity Type

Non-Profit

Font styles to use
Sans Serif

Requirements
Must have
• I need the attached logos to be included in the design, and the bottom or around the edges. Choose one of the three Kelp Lane logos, not all of them. Also the words "Thornfield Public Stewardship Alliance" (treat that as a logo like the others, since they don't have one).

```html
<!DOCTYPE html>
<html lang="en">
<head>
<meta charset="utf-8">
<title>Unified Marrowby Roundtable — Halvern Policy Symposium</title>
<link rel="stylesheet" href="https://fonts.googleapis.com/css2?family=Bebas+Neue&family=Arimo:wght@400;700&display=swap">
<style>
  :root {
    --navy-deep: #06124a;
    --navy: #0b2f8a;
    --blue: #1570d0;
    --cyan: #3fdcf2;
    --cyan-bright: #6ff0ff;
    --band: rgba(4, 12, 48, 0.62);
    --white: #ffffff;
    --ink: #1d1d1d;
    --kelp: #1d8fd6;
    --oriel: #e2371f;
    --vantry: #4a4a4a;
    --fairwick: #2a2a2a;
  }
  * { margin: 0; padding: 0; box-sizing: border-box; }
  html, body {
    width: 1200px;
    height: 2605px;
    overflow: hidden;
    background: var(--white);
  }
  .banner {
    position: relative;
    width: 1200px;
    height: 2605px;
    overflow: hidden;
  }
  .backdrop {
    position: absolute;
    left: 0; top: 0;
    width: 1200px;
    height: 2338px;
    background:
      radial-gradient(ellipse 700px 900px at 1150px 80px, var(--cyan-bright) 0%, rgba(63,220,242,0.55) 35%, rgba(63,220,242,0) 75%),
      radial-gradient(ellipse 600px 500px at 1100px 2050px, var(--cyan) 0%, rgba(63,220,242,0) 80%),
      radial-gradient(ellipse 700px 900px at 350px 1100px, var(--navy) 0%, rgba(11,47,138,0) 80%),
      linear-gradient(120deg, var(--navy-deep) 0%, var(--navy) 35%, var(--blue) 65%, var(--cyan) 100%);
  }
  .title {
    position: absolute;
    left: 0; right: 0;
    top: 250px;
    text-align: center;
    font-family: "Bebas Neue", "Oswald", sans-serif;
    font-size: 238px;
    line-height: 232px;
    color: var(--white);
    letter-spacing: 2px;
    text-shadow: 0 6px 16px rgba(0, 10, 40, 0.55);
  }
  .title span { display: block; }
  .details {
    position: absolute;
    left: 0; top: 1355px;
    width: 1200px;
    height: 408px;
    background: var(--band);
    text-align: center;
    color: var(--white);
    font-family: "Arimo", "Helvetica Neue", Arial, sans-serif;
    font-weight: 400;
    padding-top: 38px;
  }
  .details .forum { font-size: 72px; line-height: 96px; }
  .details .city { font-size: 72px; line-height: 104px; }
  .details .date { font-size: 66px; line-height: 112px; }
  .partners {
    position: absolute;
    left: 0; top: 2338px;
    width: 1200px;
    height: 267px;
    background: var(--white);
    display: flex;
    align-items: center;
    justify-content: center;
    gap: 38px;
    font-family: "Arimo", "Helvetica Neue", Arial, sans-serif;
    font-weight: 700;
    padding-bottom: 10px;
  }
  .partner { display: flex; align-items: center; gap: 12px; }
  .partner-mark { display: block; }
  .partner-kelp { color: var(--kelp); font-size: 34px; }
  .partner-oriel { color: var(--oriel); font-size: 30px; }
  .partner-vantry { color: var(--vantry); font-size: 28px; }
  .partner-fairwick { color: var(--fairwick); font-size: 28px; }
  .partner-thornfield {
    color: var(--ink);
    font-size: 17px;
    line-height: 22px;
    text-transform: uppercase;
    max-width: 230px;
  }
</style>
</head>
<body>
<main class="banner">
  <div class="backdrop" role="img" aria-label="Glowing blue world map with network connection lines and binary digits fading across it"></div>

  <h1 class="title">
    <span>Unified</span>
    <span>Marrowby</span>
    <span>Roundtable</span>
  </h1>

  <section class="details">
    <p class="forum">Halvern Policy Symposium</p>
    <p class="city">Guadalajara</p>
    <p class="date">December 2016</p>
  </section>

  <footer class="partners">
    <div class="partner partner-kelp">
      <svg class="partner-mark" width="26" height="26" viewBox="0 0 26 26"><rect width="26" height="26" fill="var(--kelp)"/></svg>
      <span>Kelp Lane</span>
    </div>
    <div class="partner partner-oriel">
      <svg class="partner-mark" width="28" height="28" viewBox="0 0 28 28"><circle cx="14" cy="14" r="14" fill="var(--oriel)"/></svg>
      <span>Oriel Commons</span>
    </div>
    <div class="partner partner-vantry"><span>Vantry Circle</span></div>
    <div class="partner partner-fairwick">
      <svg class="partner-mark" width="26" height="26" viewBox="0 0 26 26"><circle cx="13" cy="13" r="13" fill="var(--fairwick)"/></svg>
      <span>Fairwick Network</span>
    </div>
    <div class="partner partner-thornfield"><span>Thornfield Public Stewardship Alliance</span></div>
  </footer>
</main>
</body>
</html>
```